Bolvarin Incorporated

Bolvarin is a business that provides consulting, and manages and supplies trades persons in the construction and heavy industries sector. We build, do maintenance, install machinery, and can manage projects or jobs. Would like or prefer more clean, classic designs. Blacks/greys, but open to almost anything.

Target Market(s)

Industrial/Construction/Manufacturing

Industry/Entity Type

Construction Company

Contact Information for Business Card

Clean, business name on the front, possibly have the details on the back, but open to any ideas.

Logo Text

We currently do not have a slogan, open to ideas

Font styles to use
Serif
Sans Serif

Colors

Designer to choose colors to be used in the design.

Requirements
Should not have
• the oval is not my logo, was just an idea. please don't send 20 designs with the oval

```html
<!DOCTYPE html>
<html lang="en">
<head>
<meta charset="utf-8">
<title>Bolvarin Incorporated – Business Card</title>
<link href="https://fonts.googleapis.com/css2?family=Poppins:wght@400;500;600&family=Roboto:wght@400&display=swap" rel="stylesheet">
<style>
  :root {
    --stage: #2a2a2a;
    --card: #262626;
    --card-edge: #1c1c1c;
    --ink-light: #f2f2f2;
    --ink-mid: #8a8a8a;
    --ink-gloss: #111111;
    --rule: #9a9a9a;
  }
  * { margin: 0; padding: 0; box-sizing: border-box; }
  html, body { width: 1200px; height: 880px; overflow: hidden; }
  body {
    background: var(--stage);
    font-family: "Roboto", sans-serif;
    position: relative;
  }
  .card {
    position: absolute;
    width: 620px;
    height: 354px;
    background: linear-gradient(160deg, #2c2c2c 0%, var(--card) 55%, var(--card-edge) 100%);
    box-shadow: 0 18px 40px rgba(0,0,0,0.55);
  }
  .card--front { left: 60px; top: 60px; }
  .card--back { left: 520px; top: 466px; }

  .wordmark {
    font-family: "Poppins", sans-serif;
    font-weight: 500;
    letter-spacing: -0.3px;
    line-height: 1.05;
  }
  .card--front .wordmark {
    position: absolute;
    left: 0; right: 0; top: 118px;
    text-align: center;
    font-size: 42px;
    white-space: nowrap;
    color: var(--ink-gloss);
  }
  .card--front .website {
    position: absolute;
    left: 0; right: 0; top: 246px;
    text-align: center;
    font-size: 14px;
    color: var(--ink-gloss);
  }

  .card--back .wordmark {
    position: absolute;
    left: 56px; top: 148px;
    width: 230px;
    font-size: 30px;
    color: var(--ink-light);
  }
  .divider {
    position: absolute;
    left: 306px; top: 92px;
    width: 1px; height: 136px;
    background: var(--rule);
  }
  .contact {
    position: absolute;
    left: 330px; top: 84px;
    width: 270px;
  }
  .contact__name {
    font-family: "Poppins", sans-serif;
    font-weight: 600;
    font-size: 26px;
    color: var(--ink-light);
    line-height: 1.1;
  }
  .contact__name .first { color: var(--ink-mid); }
  .contact__title {
    font-family: "Poppins", sans-serif;
    font-size: 15px;
    color: var(--ink-mid);
    margin-bottom: 10px;
  }
  .contact__row {
    display: flex;
    align-items: center;
    font-size: 14px;
    color: var(--ink-light);
    line-height: 22px;
    white-space: nowrap;
  }
  .contact__icon {
    display: block;
    flex: none;
    width: 12px;
    height: 12px;
    margin-right: 10px;
    fill: var(--ink-mid);
  }
  .address {
    position: absolute;
    left: 0; right: 0; bottom: 46px;
    text-align: center;
    font-size: 14px;
    color: var(--ink-light);
  }
</style>
</head>
<body>
  <section class="card card--front">
    <div class="wordmark">Bolvarin Incorporated</div>
    <div class="website">www.Bolvarin.com</div>
  </section>

  <section class="card card--back">
    <div class="wordmark">Bolvarin<br>Incorporated</div>
    <div class="divider"></div>
    <div class="contact">
      <div class="contact__name"><span class="first">Daniel</span> Harrow</div>
      <div class="contact__title">Managing Director</div>
      <div class="contact__row">
        <svg class="contact__icon" width="12" height="12" viewBox="0 0 24 24"><path d="M6.6 10.8a15.1 15.1 0 0 0 6.6 6.6l2.2-2.2a1 1 0 0 1 1-.25 11.4 11.4 0 0 0 3.6.57 1 1 0 0 1 1 1V20a1 1 0 0 1-1 1A17 17 0 0 1 3 4a1 1 0 0 1 1-1h3.5a1 1 0 0 1 1 1c0 1.25.2 2.45.57 3.57a1 1 0 0 1-.25 1z"/></svg>
        <span>555 013 4872</span>
      </div>
      <div class="contact__row">
        <svg class="contact__icon" width="12" height="12" viewBox="0 0 24 24"><path d="M2 5h20v14H2zm2 2v.5l8 5 8-5V7zm0 2.9V17h16V9.9l-8 5z"/></svg>
        <span>dharrow@mailbox.com</span>
      </div>
      <div class="contact__row">
        <svg class="contact__icon" width="12" height="12" viewBox="0 0 24 24"><circle cx="12" cy="12" r="10"/></svg>
        <span>www.bolvarin.com</span>
      </div>
    </div>
    <div class="address">118 Calder Street, Suite 200, Northfield, MI 49000</div>
  </section>
</body>
</html>
```